Webpage Needed for Bright Harbor Wiring Electrical and Security

We need a web design for our company showing people we arent just a small business. We want to look big so people can trust us. I would like information from my business cards on the page. example, we do all house rennovations, construction, commercial, 24 hour emergency service, new installations, repairs, maintenance, home theatre and so on...

I would also like images from my facebook on the page and linked. facebook.com/brightharborwiring

Target Market(s)

builders, residents,

Industry/Entity Type

Business

Number of Pages Required

1 page

Font styles to use
Other font styles liked:
• Juice bold

Requirements
Must have
• colours the same as the logo. background must be white. also the font must be Juice Bold which is the font of the logo
Should not have
• black as the background

```html
<!DOCTYPE html>
<html lang="en">
<head>
<meta charset="utf-8">
<title>Bright Harbor Wiring Electrical and Security</title>
<link rel="stylesheet" href="https://fonts.googleapis.com/css2?family=Jura:wght@400;500;600;700&family=Baumans&display=swap">
<style>
:root{
  --orange:#f4895b;
  --orange-band:#e9875f;
  --blue:#4bb9e3;
  --cream:#f2c9a0;
  --ink:#555a60;
  --grey:#8b8e93;
  --soft:#f7f6fb;
  --white:#ffffff;
  --social:#a9adb3;
  --partner:#c9cacd;
}
*{margin:0;padding:0;box-sizing:border-box}
html,body{width:1200px;height:2531px;overflow:hidden;background:var(--white)}
body{position:relative;font-family:"Jura",sans-serif;color:var(--ink)}
.abs{position:absolute}
.center{left:0;width:1200px;text-align:center}

/* header */
.header{top:0;left:0;width:1200px;height:162px;background:var(--white)}
.social-top{top:22px;left:178px;display:flex;gap:16px}
.social-top span{width:14px;height:14px;border-radius:50%;background:var(--social);display:block}
.brand{top:16px;left:450px;width:300px;text-align:center;font-weight:700;font-size:36px;line-height:38px;color:var(--ink)}
.phone{top:14px;left:800px;display:flex;align-items:center;gap:10px;font-weight:600;font-size:32px;color:var(--ink)}
.nav{top:88px;font-size:21px;letter-spacing:1px;color:#a7aaaf;font-weight:500}
.nav.active{color:var(--orange)}
.nav-dot{top:98px;width:8px;height:8px;border-radius:50%;background:var(--orange)}

/* hero */
.hero{top:162px;left:0;width:1200px;height:430px;background:linear-gradient(90deg,#8d8f92 0%,#5f6164 35%,#2a2b2e 60%,#141517 100%)}
.hero-line{left:663px;width:360px;text-align:center;font-family:"Baumans",sans-serif;font-size:56px;line-height:60px;letter-spacing:1px}
.band{top:592px;left:0;width:1200px;height:96px;background:var(--orange-band)}
.band-item{top:608px;width:200px;text-align:center;color:var(--white);font-weight:700;font-size:14px;letter-spacing:.5px}
.band-item svg{display:block;margin:0 auto 6px}
.band-sep{top:616px;width:1px;height:56px;background:rgba(255,255,255,.5)}

/* sections */
.about{top:688px;left:0;width:1200px;height:215px;background:var(--soft)}
.kicker{font-size:11px;color:var(--orange);letter-spacing:1px;text-transform:lowercase}
.heading{font-size:40px;font-weight:600;color:var(--orange);letter-spacing:1px}
.about-text{top:768px;font-size:11.5px;line-height:25px;letter-spacing:1px;text-transform:uppercase;color:var(--ink);font-weight:600}
.read-more{top:868px;font-size:10px;letter-spacing:1.5px;color:var(--ink);font-weight:600}

.service{width:200px;text-align:center}
.service-label{font-size:11px;line-height:16px;letter-spacing:1px;font-weight:700;text-transform:uppercase;color:var(--ink)}
.service-icon{width:102px;height:102px;border-radius:50%;background:var(--orange);margin:20px auto 0;display:flex;align-items:center;justify-content:center}

.partners{top:1543px;left:0;width:1200px;height:257px;background:var(--soft)}
.partner{top:1680px;height:58px;background:var(--partner)}

.quote{top:1941px;left:333px;width:570px;font-size:16px;line-height:27px;text-align:center;color:var(--ink);font-weight:500}
.quote-mark{top:1926px;left:312px;font-family:"Baumans",sans-serif;font-size:40px;color:var(--orange)}
.dots{top:2078px;left:563px;display:flex;gap:6px}
.dots span{width:12px;height:12px;border-radius:50%;border:1.5px solid #b9bcc0}
.dots span.on{background:var(--orange);border-color:var(--orange)}

.map{top:2187px;left:0;width:1200px;height:273px;background:linear-gradient(180deg,#77797c,#626467)}
.loc{color:var(--white);font-weight:700;letter-spacing:1px}
.loc-accent{color:var(--orange)}
.social-bottom{top:2370px;width:26px;height:26px;border-radius:50%;background:var(--orange)}
.footer{top:2474px;font-size:13px;color:var(--grey)}
</style>
</head>
<body>

<header class="abs header">
  <div class="abs social-top"><span></span><span></span><span></span><span></span></div>
  <div class="abs brand">Bright Harbor<br>Wiring</div>
  <div class="abs phone">
    <svg width="22" height="22" viewBox="0 0 24 24"><path fill="#f4895b" d="M6.6 10.8a15 15 0 0 0 6.6 6.6l2.2-2.2c.3-.3.7-.4 1-.2 1.1.4 2.3.6 3.6.6.6 0 1 .4 1 1V20c0 .6-.4 1-1 1A17 17 0 0 1 3 4c0-.6.4-1 1-1h3.5c.6 0 1 .4 1 1 0 1.3.2 2.5.6 3.6.1.3 0 .7-.2 1z"/></svg>
    +0400123987
  </div>
  <nav>
    <div class="abs nav active" style="left:175px">HOME</div>
    <div class="abs nav-dot" style="left:264px"></div>
    <div class="abs nav" style="left:323px">ABOUT US</div>
    <div class="abs nav" style="left:747px">SERVICES</div>
    <div class="abs nav-dot" style="left:876px"></div>
    <div class="abs nav" style="left:934px">CONTACT</div>
  </nav>
</header>

<section class="abs hero" role="img" aria-label="Company service van with ladder parked in a workshop, lettered with the business name and phone number"></section>
<div class="abs hero-line" style="top:250px;color:var(--blue)">maintenance</div>
<div class="abs hero-line" style="top:318px;color:var(--cream)">Industrial</div>
<div class="abs hero-line" style="top:388px;color:var(--blue)">Commercial</div>
<div class="abs hero-line" style="top:457px;color:#e6e6e6">Residential</div>

<section class="abs band" role="img" aria-label="Orange-tinted photo strip of work sites"></section>
<div class="abs band-item" style="left:151px">
  <svg width="46" height="38" viewBox="0 0 46 40"><path fill="#fff" d="M6 30a17 17 0 0 1 34 0h4v4H2v-4zM20 10h6v14h-6z"/></svg>CONSTRUCTION</div>
<div class="abs band-sep" style="left:365px"></div>
<div class="abs band-item" style="left:370px">
  <svg width="46" height="38" viewBox="0 0 46 40"><path fill="#fff" d="M14 4h18v34H14zM18 8v4h3V8zm7 0v4h3V8zm-7 8v4h3v-4zm7 0v4h3v-4zm-7 8v4h3v-4zm7 0v4h3v-4z" fill-rule="evenodd"/></svg>COMMERCIAL</div>
<div class="abs band-sep" style="left:580px"></div>
<div class="abs band-item" style="left:575px">
  <svg width="46" height="38" viewBox="0 0 46 40"><circle cx="23" cy="20" r="16" fill="#fff"/><path d="M14 14l18 12M30 12l-14 16" stroke="#e9875f" stroke-width="4"/></svg>MAINTENANCE</div>
<div class="abs band-sep" style="left:786px"></div>
<div class="abs band-item" style="left:794px">
  <svg width="46" height="38" viewBox="0 0 46 40"><circle cx="23" cy="20" r="13" fill="none" stroke="#fff" stroke-width="8" stroke-dasharray="5 3.2"/><circle cx="23" cy="20" r="10" fill="#fff"/><circle cx="23" cy="20" r="4" fill="#e9875f"/></svg>NEW INSTALLATIONS</div>

<section class="abs about" aria-labelledby="about-title"></section>
<div class="abs center kicker" style="top:710px;left:-72px">know</div>
<h2 class="abs center heading" id="about-title" style="top:718px">ABOUT US</h2>
<p class="abs center about-text">We cover all new electrical installations, repairs, maintenance, renovations/extensions,<br>re-wiring, home theatre, surround sound, wall tv's, electric hot water, stoves, cooktops, lighting,<br>ceiling fans, data, telephone and security systems.</p>
<div class="abs center read-more">— READ MORE —</div>

<div class="abs center kicker" style="top:940px;left:-67px">our</div>
<h2 class="abs center heading" style="top:948px">SERVICES</h2>

<div class="abs service" style="left:119px;top:1023px"><div class="service-label">24 / 7</div><div class="service-icon"><svg width="56" height="56" viewBox="0 0 56 56"><circle cx="28" cy="28" r="22" fill="none" stroke="#fff" stroke-width="4"/><path d="M28 14v14l10 6" stroke="#fff" stroke-width="4" fill="none"/></svg></div></div>
<div class="abs service" style="left:307px;top:1023px"><div class="service-label">Home Theatre</div><div class="service-icon"><svg width="56" height="56" viewBox="0 0 56 56"><path fill="#fff" d="M8 22h40v24H8zM8 12l38-6 1 8-38 6z"/></svg></div></div>
<div class="abs service" style="left:497px;top:1023px"><div class="service-label">Electric Hot Water</div><div class="service-icon"><svg width="56" height="56" viewBox="0 0 56 56"><path fill="#fff" d="M28 6c8 12 14 20 14 28a14 14 0 0 1-28 0c0-8 6-16 14-28z"/></svg></div></div>
<div class="abs service" style="left:687px;top:1023px"><div class="service-label">New Intsallations</div><div class="service-icon"><svg width="56" height="56" viewBox="0 0 56 56"><path fill="#fff" d="M23 6h10v18h8L28 38 15 24h8zM6 36h8v8h28v-8h8v14H6z"/></svg></div></div>
<div class="abs service" style="left:875px;top:1023px"><div class="service-label">Stoves</div><div class="service-icon"><svg width="56" height="56" viewBox="0 0 56 56"><ellipse cx="28" cy="36" rx="22" ry="10" fill="none" stroke="#fff" stroke-width="3"/><ellipse cx="28" cy="36" rx="12" ry="5" fill="none" stroke="#fff" stroke-width="3"/><path d="M22 24c-3-5 3-8 0-14M30 24c-3-5 3-8 0-14" stroke="#fff" stroke-width="3" fill="none"/></svg></div></div>

<div class="abs service" style="left:119px;top:1187px"><div class="service-label">Repairs</div><div class="service-icon"><svg width="56" height="56" viewBox="0 0 56 56"><path d="M12 46l20-20" stroke="#fff" stroke-width="7" stroke-linecap="round"/><circle cx="37" cy="19" r="11" fill="#fff"/><circle cx="42" cy="14" r="5" fill="#f4895b"/></svg></div></div>
<div class="abs service" style="left:307px;top:1187px"><div class="service-label">Cooktops</div><div class="service-icon"><svg width="56" height="56" viewBox="0 0 56 56"><rect x="10" y="8" width="36" height="40" rx="4" fill="none" stroke="#fff" stroke-width="4"/><path d="M10 18h36M17 28h22M17 36h22" stroke="#fff" stroke-width="3"/></svg></div></div>
<div class="abs service" style="left:497px;top:1187px"><div class="service-label">Maintenance</div><div class="service-icon"><svg width="56" height="56" viewBox="0 0 56 56"><path fill="#fff" d="M14 20a14 14 0 0 1 28 0zM10 48c2-10 9-14 18-14s16 4 18 14z"/><path d="M40 30l8-8" stroke="#fff" stroke-width="4"/></svg></div></div>
<div class="abs service" style="left:687px;top:1187px"><div class="service-label">Lighting</div><div class="service-icon"><svg width="56" height="56" viewBox="0 0 56 56"><path d="M28 8a13 13 0 0 0-7 24v6h14v-6a13 13 0 0 0-7-24z" fill="none" stroke="#fff" stroke-width="3"/><path d="M22 43h12M24 48h8" stroke="#fff" stroke-width="3"/></svg></div></div>
<div class="abs service" style="left:875px;top:1187px"><div class="service-label">Renovations</div><div class="service-icon"><svg width="56" height="56" viewBox="0 0 56 56"><path fill="#fff" d="M28 8l22 20h-6v20H33V36H23v12H12V28H6z"/></svg></div></div>

<div class="abs service" style="left:119px;top:1353px"><div class="service-label">Re-Wiring</div><div class="service-icon"><svg width="56" height="56" viewBox="0 0 56 56"><path d="M10 46l24-24M14 50l28-20M8 40l20-28M34 22l12-14M42 30l10-6" stroke="#fff" stroke-width="3" fill="none" stroke-linecap="round"/></svg></div></div>
<div class="abs service" style="left:307px;top:1353px"><div class="service-label">Testing and Tagging</div><div class="service-icon"><svg width="56" height="56" viewBox="0 0 56 56"><path d="M10 46l16-16" stroke="#fff" stroke-width="8" stroke-linecap="round"/><path d="M28 28l16-16" stroke="#fff" stroke-width="4" stroke-linecap="round"/></svg></div></div>
<div class="abs service" style="left:497px;top:1353px"><div class="service-label">Surround Sound</div><div class="service-icon"><svg width="56" height="56" viewBox="0 0 56 56"><ellipse cx="28" cy="28" rx="14" ry="20" fill="none" stroke="#fff" stroke-width="4"/><ellipse cx="28" cy="28" rx="5" ry="8" fill="#fff"/></svg></div></div>
<div class="abs service" style="left:687px;top:1353px"><div class="service-label">Telephone</div><div class="service-icon"><svg width="48" height="48" viewBox="0 0 24 24"><path fill="#fff" d="M6.6 10.8a15 15 0 0 0 6.6 6.6l2.2-2.2c.3-.3.7-.4 1-.2 1.1.4 2.3.6 3.6.6.6 0 1 .4 1 1V20c0 .6-.4 1-1 1A17 17 0 0 1 3 4c0-.6.4-1 1-1h3.5c.6 0 1 .4 1 1 0 1.3.2 2.5.6 3.6.1.3 0 .7-.2 1z"/></svg></div></div>
<div class="abs service" style="left:875px;top:1353px"><div class="service-label">Wall TV,S</div><div class="service-icon"><svg width="56" height="56" viewBox="0 0 56 56"><rect x="8" y="12" width="40" height="26" rx="2" fill="none" stroke="#fff" stroke-width="4"/><path d="M20 46h16M28 38v8" stroke="#fff" stroke-width="4"/></svg></div></div>

<section class="abs partners" aria-labelledby="partners-title"></section>
<div class="abs center kicker" style="top:1560px;left:-65px">our</div>
<h2 class="abs center heading" id="partners-title" style="top:1568px">PARTNERS</h2>
<div class="abs partner" style="left:192px;width:98px"></div>
<div class="abs partner" style="left:395px;width:160px;height:36px;top:1692px"></div>
<div class="abs partner" style="left:634px;width:150px;height:40px;top:1690px"></div>
<div class="abs partner" style="left:864px;width:156px;height:40px;top:1690px"></div>

<div class="abs center kicker" style="top:1830px;left:-92px">client</div>
<h2 class="abs center heading" style="top:1838px">TESTIMONIALS</h2>
<div class="abs quote-mark">“</div>
<p class="abs quote">Lorem ipsum dolor sit amet, consectetuer adipiscing elit, sed diam nonummy nibh euismod tincidunt ut laoreet dolore magna aliquam erat volutpat. Ut wisi enim ad minim veniam, quis nostrud exerci tation ullamcorper suscipit lobortis nisl ut aliquip ex ea commodo consequat.</p>
<div class="abs dots"><span class="on"></span><span></span><span></span><span></span></div>

<h2 class="abs center heading" style="top:2128px">LOCATE US</h2>
<section class="abs map" role="img" aria-label="Street map of the local service area"></section>
<div class="abs center loc" style="top:2224px;font-size:18px">WE ARE AVAILABLE 24/7</div>
<div class="abs center loc loc-accent" style="top:2265px;font-size:12px">LENA MARSH</div>
<div class="abs center loc" style="top:2291px;font-size:12px">HARBOURSIDE, NEW SOUTH WALES, <span class="loc-accent">AUSTRALIA 2000</span></div>
<div class="abs center loc" style="top:2320px;font-size:12px">+0400123987 / <span class="loc-accent">LENA@BRIGHTHARBORWIRING.COM.AU</span></div>
<div class="abs social-bottom" style="left:327px"></div>
<div class="abs social-bottom" style="left:449px"></div>
<div class="abs social-bottom" style="left:580px"></div>
<div class="abs social-bottom" style="left:710px"></div>
<div class="abs social-bottom" style="left:839px"></div>

<footer class="abs center footer">© 2015 All rights reserved brightharborwiring.com.au</footer>
</body>
</html>
```